existing Business Card Re design

We are wanting to re design our cards to reflect our new logo , i have attache the current business cards and new logo
i will need a business card that reflects the following information on each card.

card 1:
Harold Dunsby, President
555-382-9164
info@kpqfoamcoat.com

card 2:
Colin Thresher, Outside Sales
Office: 555-382-9164
Cell: 555-617-2048
Sales@kpqfoamcoat.com

Card 3
Louis Varcoe, Branch Manager
Office: 555-382-9164
Cell: 555-493-7752
Louis@kpqfoamcoat.com

Card 4
I will need a Generic card with no name on it just business
555-382-9164
info@kpqfoamcoat.com

Target Market(s)

Homeowners and Contractors

Contact Information for Business Card

We are wanting to re design our cards to reflect our new logo , i have attache the current business cards and new logo. same info on current card

card 1:
Harold Dunsby, President
555-382-9164
info@kpqfoamcoat.com

card 2:
Office: 555-382-9164
Cell: 555-617-2048
Sales@kpqfoamcoat.com

Card 3
Office: 555-382-9164
Cell: 555-493-7752
Louis@kpqfoamcoat.com

Card 4
555-382-9164
info@kpqfoamcoat.com

Requirements
Must have
• same info as current cards with a added business
"sanitizing"

```html
<!DOCTYPE html>
<html lang="en">
<head>
<meta charset="UTF-8">
<title>Keystone Foam Coat – Business Card</title>
<link href="https://fonts.googleapis.com/css2?family=Montserrat:wght@800&family=Open+Sans:wght@400&display=swap" rel="stylesheet">
<style>
  :root {
    --page-bg: #eceeef;
    --card-white: #ffffff;
    --card-dark: #2c2c2c;
    --brand-blue: #1a9be0;
    --brand-navy: #0e2f6e;
    --text-grey: #4a4a4a;
    --rule-grey: #7a7a7a;
    --emboss: #232323;
  }
  * { margin: 0; padding: 0; box-sizing: border-box; }
  html, body { width: 1200px; height: 857px; overflow: hidden; }
  body {
    background: var(--page-bg);
    position: relative;
    font-family: "Open Sans", Arial, sans-serif;
  }
  .card {
    position: absolute;
    top: 280px;
    width: 520px;
    height: 297px;
    border-bottom: 4px solid var(--brand-blue);
    box-shadow: 0 10px 28px rgba(0,0,0,0.18);
  }
  .card-front { left: 50px; background: var(--card-white); }
  .card-back { left: 630px; background: var(--card-dark); }

  .brand {
    position: absolute;
    left: 30px;
    top: 0;
    width: 250px;
    height: 100%;
    display: flex;
    align-items: center;
    gap: 9px;
  }
  .brand-square {
    width: 20px; height: 20px;
    flex: none;
    background: var(--brand-blue);
  }
  .brand-name {
    font-family: "Montserrat", Arial, sans-serif;
    font-weight: 800;
    font-size: 19px;
    color: var(--brand-navy);
    white-space: nowrap;
  }
  .divider {
    position: absolute;
    left: 300px;
    top: 82px;
    width: 1px;
    height: 110px;
    background: var(--rule-grey);
  }
  .contact {
    position: absolute;
    left: 322px;
    top: 78px;
  }
  .person-name {
    font-family: "Montserrat", Arial, sans-serif;
    font-weight: 800;
    font-size: 18px;
    color: var(--brand-blue);
    line-height: 1.1;
  }
  .person-title {
    font-size: 12px;
    color: var(--text-grey);
    margin-top: 2px;
    margin-bottom: 14px;
  }
  .contact-list { list-style: none; }
  .contact-item {
    display: flex;
    align-items: center;
    gap: 8px;
    font-size: 11.5px;
    color: var(--text-grey);
    line-height: 1.75;
    white-space: nowrap;
  }
  .contact-icon { width: 11px; height: 11px; flex: none; }

  .back-brand {
    position: absolute;
    inset: 0;
    display: flex;
    align-items: center;
    justify-content: center;
    font-family: "Montserrat", Arial, sans-serif;
    font-weight: 800;
    font-size: 30px;
    color: var(--emboss);
    white-space: nowrap;
  }
</style>
</head>
<body>
  <section class="card card-front" aria-label="Business card front">
    <div class="brand">
      <span class="brand-square"></span>
      <span class="brand-name">Keystone Foam Coat</span>
    </div>
    <div class="divider"></div>
    <div class="contact">
      <p class="person-name">Harold Dunsby</p>
      <p class="person-title">President</p>
      <ul class="contact-list">
        <li class="contact-item">
          <svg class="contact-icon" viewBox="0 0 12 12"><circle cx="6" cy="6" r="6" fill="#1a9be0"/><path d="M4 3.2l1.1 1.3-.6.7c.4.9 1.1 1.6 2 2l.7-.6 1.3 1.1-.7.9C5.9 8.5 3.6 6.2 3.4 3.9z" fill="#fff"/></svg>
          555-382-9164
        </li>
        <li class="contact-item">
          <svg class="contact-icon" viewBox="0 0 12 12"><circle cx="6" cy="6" r="6" fill="#1a9be0"/><rect x="3" y="4" width="6" height="4.2" fill="#fff"/><path d="M3 4l3 2.3L9 4" stroke="#1a9be0" stroke-width="0.7" fill="none"/></svg>
          info@kpqfoamcoat.com
        </li>
        <li class="contact-item">
          <svg class="contact-icon" viewBox="0 0 12 12"><circle cx="6" cy="6" r="6" fill="#1a9be0"/><circle cx="6" cy="6" r="3" fill="none" stroke="#fff" stroke-width="0.8"/><path d="M3 6h6M6 3c-1.2 1.6-1.2 4.4 0 6M6 3c1.2 1.6 1.2 4.4 0 6" stroke="#fff" stroke-width="0.6" fill="none"/></svg>
          www.kpqfoamcoat.com
        </li>
      </ul>
    </div>
  </section>

  <section class="card card-back" aria-label="Business card back">
    <p class="back-brand">Keystone Foam Coat</p>
  </section>
</body>
</html>
```